Property Management Company Business Cards

Need business cards for a property management company located in Michigan. We manage houses for clients all over the world. Young and modern company, looking for eye catching design. Please work with the attached logo.

Industry/Entity Type

Property Management

Requirements
Must have
• Need lines for address, telephone number, fax number, web site.

Also lines for name, and job title

```html
<!DOCTYPE html>
<html lang="en">
<head>
<meta charset="utf-8">
<title>Lakeshore Harbor Management – Business Cards</title>
<link href="https://fonts.googleapis.com/css2?family=Open+Sans:wght@400;700&display=swap" rel="stylesheet">
<style>
  :root {
    --backdrop: #3a3a3c;
    --card-white: #ffffff;
    --brand-blue: #1ea3cb;
    --ink-dark: #333436;
    --ink-grey: #6b6c6e;
  }
  * { box-sizing: border-box; margin: 0; padding: 0; }
  html, body {
    width: 1200px; height: 900px; overflow: hidden;
    background: var(--backdrop);
    font-family: "Open Sans", sans-serif;
  }
  .canvas { position: relative; width: 1200px; height: 900px; }

  .card {
    position: absolute;
    width: 680px; height: 390px;
    box-shadow: 0 10px 30px rgba(0,0,0,.45);
    overflow: hidden;
  }

  /* back of card */
  .card-back {
    left: 440px; top: 50px;
    background: var(--brand-blue);
  }
  .card-back .wordmark {
    position: absolute; right: 40px; bottom: 44px;
    display: flex; align-items: center; gap: 14px;
  }
  .card-back .wordmark-text { font-size: 30px; }

  /* front of card */
  .card-front {
    left: 80px; top: 470px;
    background: var(--card-white);
  }
  .accent-bar {
    position: absolute; left: 0; top: 150px;
    width: 10px; height: 240px;
    background: var(--brand-blue);
  }
  .card-front .wordmark {
    position: absolute; right: 44px; top: 40px;
    display: flex; align-items: center; gap: 10px;
  }
  .card-front .wordmark-text { font-size: 21px; }

  .wordmark-text {
    font-weight: 700; color: var(--ink-dark);
    line-height: 1.05; text-transform: uppercase; letter-spacing: .5px;
  }
  .wordmark-dot {
    border-radius: 50%; background: var(--ink-dark); flex: none;
  }
  .card-back .wordmark-dot { width: 44px; height: 44px; }
  .card-front .wordmark-dot { width: 30px; height: 30px; }

  .contact {
    position: absolute; left: 48px; top: 120px;
    color: var(--ink-grey); font-size: 15px; line-height: 1.4;
  }
  .person-name { font-size: 22px; font-weight: 700; color: var(--ink-dark); }
  .person-title { margin-bottom: 18px; }
  .address { margin-bottom: 18px; }
  .lines { display: flex; gap: 40px; }
  .line { display: flex; align-items: center; gap: 8px; }
  .line svg { width: 14px; height: 14px; flex: none; }
  .lines-online { margin-top: 22px; }
</style>
</head>
<body>
<div class="canvas">

  <section class="card card-back">
    <div class="wordmark">
      <span class="wordmark-dot"></span>
      <span class="wordmark-text">Lakeshore Harbor<br>Management</span>
    </div>
  </section>

  <section class="card card-front">
    <div class="accent-bar"></div>

    <div class="wordmark">
      <span class="wordmark-dot"></span>
      <span class="wordmark-text">Lakeshore Harbor<br>Management</span>
    </div>

    <div class="contact">
      <p class="person-name">Daniel Foster</p>
      <p class="person-title">Marketing Manager</p>
      <p class="address">PO Box 618<br>Fairview SA 5091</p>

      <div class="lines">
        <div>
          <p class="line">
            <svg viewBox="0 0 16 16" aria-hidden="true"><path fill="#1ea3cb" d="M3 2h3l1 4-2 1a9 9 0 0 0 4 4l1-2 4 1v3c0 1-1 1-1 1A12 12 0 0 1 2 3s0-1 1-1z"/></svg>
            (08) 8340 5512
          </p>
          <p class="line">
            <svg viewBox="0 0 16 16" aria-hidden="true"><rect x="4" y="1" width="8" height="14" rx="1.5" fill="none" stroke="#1ea3cb" stroke-width="1.6"/><circle cx="8" cy="12.5" r="1" fill="#1ea3cb"/></svg>
            0413 927 3680
          </p>
        </div>
        <div class="lines-online">
          <p class="line">
            <svg viewBox="0 0 16 16" aria-hidden="true"><rect x="1.5" y="3.5" width="13" height="9" fill="none" stroke="#1ea3cb" stroke-width="1.4"/><path d="M1.5 3.5 8 9l6.5-5.5" fill="none" stroke="#1ea3cb" stroke-width="1.4"/></svg>
            daniel@lakeshoreharbor.com
          </p>
          <p class="line">
            <svg viewBox="0 0 16 16" aria-hidden="true"><circle cx="8" cy="8" r="6.5" fill="none" stroke="#1ea3cb" stroke-width="1.4"/><ellipse cx="8" cy="8" rx="3" ry="6.5" fill="none" stroke="#1ea3cb" stroke-width="1.2"/><path d="M1.5 8h13" stroke="#1ea3cb" stroke-width="1.2"/></svg>
            www.lakeshoreharbor.com
          </p>
        </div>
      </div>
    </div>
  </section>

</div>
</body>
</html>
```